The maple crew

I want it as prefession and attractive as possible we are a lawnmowing business

Phone number 605-318-2264
Name- Carlos Whitfield
Email- themaplecrewsd@fernpost.com

```html
<!DOCTYPE html>
<html lang="en">
<head>
<meta charset="UTF-8">
<title>The Maple Crew – Business Card</title>
<link href="https://fonts.googleapis.com/css2?family=Saira+Condensed:wght@600;800&family=Montserrat:wght@400&display=swap" rel="stylesheet">
<style>
  :root {
    --canvas: #e4e4e4;
    --green-deep: #1f5e34;
    --green-mid: #2f7a45;
    --green-soft: #4a9a5e;
    --green-bright: #6ed36a;
    --white: #ffffff;
    --ink-green: #2a7a3f;
  }
  * { box-sizing: border-box; margin: 0; padding: 0; }
  html, body { width: 1200px; height: 900px; overflow: hidden; }
  body {
    background: var(--canvas);
    display: flex;
    align-items: center;
    justify-content: center;
    gap: 60px;
  }
  .card {
    position: relative;
    width: 500px;
    height: 286px;
    border-radius: 22px;
    overflow: hidden;
    box-shadow: 0 10px 24px rgba(0,0,0,0.18);
  }
  /* Front */
  .card-front .grass-photo {
    position: absolute; inset: 0;
    background: radial-gradient(ellipse at 40% 45%, var(--green-soft), var(--green-mid) 55%, var(--green-deep));
  }
  .brand-lockup {
    position: absolute;
    left: 50%; top: 50%;
    transform: translate(-50%, -50%);
    display: flex;
    align-items: center;
    gap: 14px;
  }
  .brand-mark {
    width: 26px; height: 26px;
    background: var(--white);
  }
  .brand-name {
    font-family: 'Saira Condensed', sans-serif;
    font-weight: 800;
    font-size: 54px;
    letter-spacing: 1px;
    text-transform: uppercase;
    color: var(--white);
    white-space: nowrap;
  }
  /* Back */
  .card-back { background: var(--white); }
  .card-back .lawn-scene {
    position: absolute;
    left: 0; right: 0; bottom: 0;
    height: 200px;
    background: linear-gradient(180deg, var(--green-mid), var(--green-deep));
  }
  .card-back .brand-name-small {
    position: absolute;
    left: 26px; top: 24px;
    font-family: 'Saira Condensed', sans-serif;
    font-weight: 800;
    font-size: 30px;
    text-transform: uppercase;
    color: var(--ink-green);
    white-space: nowrap;
  }
  .contact {
    position: absolute;
    left: 30px; top: 118px;
  }
  .contact-name {
    font-family: 'Saira Condensed', sans-serif;
    font-weight: 600;
    font-size: 26px;
    letter-spacing: 1px;
    text-transform: uppercase;
    color: var(--green-bright);
    padding-left: 70px;
  }
  .contact-phone {
    font-family: 'Saira Condensed', sans-serif;
    font-weight: 800;
    font-size: 50px;
    line-height: 1;
    letter-spacing: 3px;
    color: var(--white);
  }
  .contact-email {
    margin-top: 8px;
    font-family: 'Montserrat', sans-serif;
    font-size: 13px;
    color: var(--white);
  }
</style>
</head>
<body>
  <section class="card card-front" aria-label="Business card front">
    <div class="grass-photo" role="img" aria-label="Close-up photograph of green lawn grass"></div>
    <div class="brand-lockup">
      <span class="brand-mark"></span>
      <span class="brand-name">The maple crew</span>
    </div>
  </section>

  <section class="card card-back" aria-label="Business card back">
    <div class="lawn-scene" role="img" aria-label="Green lawn with a silhouette of a worker pushing a lawn mower"></div>
    <div class="brand-name-small">The maple crew</div>
    <div class="contact">
      <p class="contact-name">Carlos Whitfield</p>
      <p class="contact-phone">605-318-2264</p>
      <p class="contact-email">themaplecrewsd@fernpost.com</p>
    </div>
  </section>
</body>
</html>
```